flyer design for landscape group. i have enclosed my business card with logo

we are a local domestic and commercial landscaping group based in wokingham berkshire .we offer competitive landscaping solutions with a broad knowledge helping us solve problems in many fields such as new lawns, lawn care,tree care ,tree removal,hard and soft landscaping, decking, fencing ,garden or land clearance or just helping you with general maintanence. Being fully insured and certified for the job ,our excellent attention to detail has seen us recognised by local authorities and work for them on maintenance programmes performing in a safe and efficient manner

Target Market(s)

high end gardens commercial property

Industry/Entity Type

Landscaping

Requirements
Must have
• my logo . and some minimal sleek black and white design with small injections of colour
Should not have
• please do not include my full name or address only email and telephone

```html
<!DOCTYPE html>
<html lang="en">
<head>
<meta charset="utf-8">
<title>Fernleigh Gardens – Landscaping Flyer</title>
<link rel="stylesheet" href="https://fonts.googleapis.com/css2?family=Lato:wght@400;700&family=Roboto:wght@400&family=Roboto+Condensed:wght@700&display=swap">
<style>
  :root {
    --white: #ffffff;
    --orange: #f39a1e;
    --orange-light: #f8c531;
    --green: #3fab3c;
    --green-light: #5cc04a;
    --green-dark: #129a47;
    --brown: #3d2414;
    --ink: #1f1f1f;
    --logo-ink: #3a2a20;
    --paper-grey: #ecebe8;
    --pill: #ececec;
  }
  * { box-sizing: border-box; margin: 0; padding: 0; }
  html, body { width: 869px; height: 1200px; overflow: hidden; background: var(--white); }
  .flyer { position: relative; width: 869px; height: 1200px; overflow: hidden; font-family: "Lato", sans-serif; }
  .flyer-art { position: absolute; inset: 0; }

  .brand { position: absolute; left: 0; width: 420px; top: 110px; text-align: center; }
  .brand-dot { display: block; width: 26px; height: 26px; border-radius: 50%; background: var(--green-dark); margin: 0 auto 22px; }
  .brand-name { font-family: "Lato", sans-serif; font-weight: 400; font-size: 40px; letter-spacing: 4px; color: var(--logo-ink); line-height: 1.1; }

  .headline { position: absolute; left: 22px; color: var(--white); line-height: 1; }
  .headline-main { top: 392px; font-family: "Roboto Condensed", sans-serif; font-weight: 700; font-size: 74px; letter-spacing: 0.5px; }
  .headline-sub { top: 481px; font-family: "Roboto", sans-serif; font-weight: 400; font-size: 34px; color: var(--ink); }
  .headline-tag { top: 541px; font-family: "Roboto Condensed", sans-serif; font-weight: 700; font-size: 36px; letter-spacing: 0.5px; }

  .services-label { position: absolute; left: 0; top: 728px; width: 213px; height: 42px; background: var(--pill); border-radius: 0 21px 21px 0; padding-left: 24px; font-family: "Roboto Condensed", sans-serif; font-weight: 700; font-size: 31px; line-height: 42px; color: var(--ink); box-shadow: 0 3px 6px rgba(0,0,0,0.15); }
  .services-list { position: absolute; left: 46px; top: 792px; list-style: none; }
  .services-list li { position: relative; padding-left: 24px; font-weight: 700; font-size: 22px; line-height: 28.7px; color: var(--ink); }
  .services-list li::before { content: ""; position: absolute; left: 0; top: 11px; width: 7px; height: 7px; border-radius: 50%; background: var(--orange-light); }

  .contact { position: absolute; left: 36px; top: 1082px; list-style: none; }
  .contact li { display: flex; align-items: center; gap: 12px; height: 30px; font-size: 19px; color: var(--white); }
  .contact svg { width: 16px; height: 16px; flex: none; }
</style>
</head>
<body>
<main class="flyer">
  <svg class="flyer-art" width="869" height="1200" viewBox="0 0 869 1200" aria-hidden="false">
    <defs>
      <linearGradient id="orangeBand" x1="0" y1="0" x2="1" y2="1">
        <stop offset="0" stop-color="#f39a1e"/>
        <stop offset="1" stop-color="#f8c531"/>
      </linearGradient>
      <linearGradient id="greenField" x1="0" y1="0" x2="1" y2="1">
        <stop offset="0" stop-color="#3fab3c"/>
        <stop offset="1" stop-color="#5cc04a"/>
      </linearGradient>
      <linearGradient id="heroTone" x1="0" y1="0" x2="1" y2="1">
        <stop offset="0" stop-color="#b9d3e0"/>
        <stop offset="0.45" stop-color="#7fa65a"/>
        <stop offset="1" stop-color="#3a4a55"/>
      </linearGradient>
      <linearGradient id="sepiaTone" x1="0" y1="0" x2="0" y2="1">
        <stop offset="0" stop-color="#c9a9a0"/>
        <stop offset="1" stop-color="#6e4d45"/>
      </linearGradient>
    </defs>

    <!-- orange headline band -->
    <path d="M0,340 C160,352 330,380 470,420 L869,420 L869,780 L0,780 Z" fill="url(#orangeBand)"/>
    <path d="M0,334 C160,346 330,372 470,412 L470,424 C330,386 160,360 0,350 Z" fill="var(--brown)"/>

    <!-- hero photo frame -->
    <ellipse cx="652" cy="288" rx="252" ry="272" fill="var(--orange)"/>
    <ellipse cx="657" cy="280" rx="242" ry="264" fill="var(--green-dark)"/>
    <ellipse cx="662" cy="273" rx="233" ry="257" fill="var(--white)"/>
    <ellipse cx="665" cy="270" rx="226" ry="250" fill="url(#heroTone)" role="img" aria-label="Photo of a gardener trimming a conifer hedge with shears"/>

    <!-- lower area -->
    <path d="M0,770 C250,700 600,690 869,752 L869,1200 L0,1200 Z" fill="var(--paper-grey)" role="img" aria-label="Faint leaf texture background"/>
    <path d="M0,770 C250,700 600,690 869,752 L869,766 C600,706 250,716 0,784 Z" fill="var(--brown)"/>
    <path d="M0,784 C200,730 420,712 560,712 C520,820 470,1000 440,1200 L0,1200 Z" fill="var(--orange)"/>
    <path d="M0,784 C200,730 410,716 540,716 C500,820 450,1000 420,1200 L0,1200 Z" fill="url(#greenField)"/>

    <!-- service photo circles -->
    <circle cx="639" cy="783" r="104" fill="var(--green)"/>
    <circle cx="639" cy="783" r="92" fill="url(#sepiaTone)" role="img" aria-label="Photo of a landscaped front garden with paving"/>
    <circle cx="639" cy="1038" r="104" fill="var(--green)"/>
    <circle cx="639" cy="1038" r="92" fill="url(#sepiaTone)" role="img" aria-label="Photo of a gloved hand planting into a lawn"/>

    <!-- contact band -->
    <path d="M0,1054 C170,1040 340,1070 480,1200 L0,1200 Z" fill="var(--white)"/>
    <path d="M0,1062 C165,1050 330,1078 466,1200 L0,1200 Z" fill="var(--brown)"/>
  </svg>

  <header class="brand">
    <span class="brand-dot"></span>
    <p class="brand-name">FERNLEIGH GARDENS</p>
  </header>

  <h1 class="headline headline-main">DOMESTIC</h1>
  <p class="headline headline-sub">AND COMMERCIAL</p>
  <p class="headline headline-tag">LANDSCAPING GROUP</p>

  <h2 class="services-label">SERVICES</h2>
  <ul class="services-list">
    <li>New lawns</li>
    <li>Lawn care</li>
    <li>Tree care</li>
    <li>Tree removal</li>
    <li>Hard and soft landscaping</li>
    <li>Decking</li>
    <li>Fencing</li>
    <li>Garden or land clearance</li>
  </ul>

  <ul class="contact">
    <li>
      <svg viewBox="0 0 16 16"><path d="M3.5 1.5l2.5 0 1 3.5-1.6 1.2c.8 1.7 2.1 3 3.8 3.8L10.4 8.4l3.5 1v2.5c0 .9-.8 1.6-1.7 1.5C6.7 13 2.9 9.3 2.1 3.3 2 2.3 2.6 1.5 3.5 1.5z" fill="var(--orange-light)"/></svg>
      <span>0770 314 5289</span>
    </li>
    <li>
      <svg viewBox="0 0 16 16"><rect x="1" y="3.5" width="14" height="9" fill="var(--orange-light)"/><path d="M1 3.5l7 5 7-5" fill="none" stroke="var(--brown)" stroke-width="1.3"/></svg>
      <span>hello@fernleighgardens.co.uk</span>
    </li>
    <li>
      <svg viewBox="0 0 16 16"><circle cx="8" cy="8" r="6.5" fill="none" stroke="var(--orange-light)" stroke-width="1.4"/><ellipse cx="8" cy="8" rx="2.8" ry="6.5" fill="none" stroke="var(--orange-light)" stroke-width="1.2"/><path d="M1.5 8h13" stroke="var(--orange-light)" stroke-width="1.2"/></svg>
      <span>www.fernleighgardens.co.uk</span>
    </li>
  </ul>
</main>
</body>
</html>
```